Business card design needed

I need a business card design for a dog walking, dog minding and dog training business. Please refer to my website for the basic company colours and fonts I'm after. Planning on a double sided card, so all information doesn't need to be on the 'front' side.
Cheers

Industry/Entity Type

Dog Training

Contact Information for Business Card

Bramble Paws - guiding hounds
Ned 0487306914
bramblepawsdemo.com.au
-walking
-holiday stays
-onsite care
-training and behavioural consultations

```html
<!DOCTYPE html>
<html lang="en">
<head>
<meta charset="utf-8">
<title>Bramble Paws – Business Card</title>
<link rel="stylesheet" href="https://fonts.googleapis.com/css2?family=Exo+2:ital,wght@0,300;0,400;0,700;1,300&display=swap">
<style>
  :root {
    --paper: #ffffff;
    --ink: #111111;
    --slate: #58585a;
    --accent: #e8582a;
    --placeholder-light: #f1efee;
    --placeholder-mid: #e4e1df;
  }
  * { margin: 0; padding: 0; box-sizing: border-box; }
  html, body {
    width: 1200px;
    height: 692px;
    overflow: hidden;
    background: var(--paper);
  }
  .card {
    position: relative;
    width: 1200px;
    height: 692px;
    overflow: hidden;
    background: var(--paper);
    font-family: "Exo 2", "Helvetica Neue", Arial, sans-serif;
    color: var(--slate);
  }
  .contact {
    position: absolute;
    right: 48px;
    top: 80px;
    text-align: right;
  }
  .contact__line {
    font-size: 62px;
    line-height: 1;
    font-weight: 300;
    letter-spacing: 0.5px;
    white-space: nowrap;
  }
  .contact__name {
    font-weight: 700;
    color: var(--ink);
  }
  .contact__area {
    margin-top: 18px;
    font-size: 41px;
    font-style: italic;
    font-weight: 300;
    white-space: nowrap;
  }
  .mascot {
    position: absolute;
    left: 0;
    top: 282px;
    width: 320px;
    height: 370px;
    background: linear-gradient(160deg, var(--placeholder-light), var(--placeholder-mid));
    border-radius: 0 18px 18px 0;
  }
  .brand {
    position: absolute;
    left: 325px;
    top: 482px;
  }
  .brand__name {
    font-size: 110px;
    line-height: 1;
    font-weight: 400;
    color: var(--accent);
    letter-spacing: 1px;
    text-transform: uppercase;
    white-space: nowrap;
  }
  .brand__tagline {
    margin-top: 0;
    font-size: 55px;
    line-height: 1;
    font-weight: 300;
    color: var(--slate);
    white-space: nowrap;
  }
</style>
</head>
<body>
  <main class="card">
    <div class="contact">
      <p class="contact__line"><span class="contact__name">Ned</span> 0487 306 914</p>
      <p class="contact__area">servicing the inner suburbs of Melbourne</p>
    </div>

    <div class="mascot" role="img" aria-label="Line drawing of a standing dog wearing a collar and leash"></div>

    <div class="brand">
      <p class="brand__name">Bramble Paws</p>
      <p class="brand__tagline">guiding hounds</p>
    </div>
  </main>
</body>
</html>
```